Clinician Harbor Collective

I am a financial planner whose client's are physicians and dentists. As physicians, there is very little time for them to do research on numerous aspects of their business and personal lives. I am looking to build a website that is a 1 stop shop for many of the services/resources they may need. It will be my job to screen the resources/advertisers and place competent people/business's that I know and have a track record on. there will ultimately be 10 or 12 ish areas that I would like to provide resources in:
disability insurance
life insurance
retirement planning
student loan advisors
employment contract and business formation attorneys
accountants
real estate agents
physician mortgages
personal loans
malpractice insurance
physician recruiters
maybe 2 other areas which I have yet to figure out.....
I would like each of these options to be able to be clicked on and a page will open up with the 1 or 2 or 3 or 4 people/business's that I have picked to represent these areas. I would like each specific person/business to have a click here to contact me link in which an email goes to the person and I am copied on the initial correspondence between the physician and the mortgage broker.... just so I can see some of the correspondence they will be receiving.
nowhere on the site do I want it to say my name. there will be certain disclosures that are needed and other wording but I think this is a good starting point.
here are links to two websites with the same general concept. please keep in mind that I want my website to be more on the simple side.
http://www.vantorelmedlink.example/index.html
http://bluestethwealth.example/
Industry/Entity Type
Financial

```html
<!DOCTYPE html>
<html lang="en">
<head>
<meta charset="utf-8">
<title>Clinician Harbor Collective</title>
<link rel="stylesheet" href="https://fonts.googleapis.com/css2?family=Open+Sans:wght@300;400;600;700;800&display=swap">
<style>
:root{
  --blue:#1f78c8;
  --blue-dark:#0f5aa0;
  --ink:#2b2b2b;
  --text:#777;
  --muted:#9a9a9a;
  --footer:#2a2a2a;
  --footer-dark:#1c1c1c;
  --red:#d21f26;
  --orange:#e07a12;
  --white:#fff;
}
*{box-sizing:border-box;margin:0;padding:0}
html,body{width:1200px;height:3126px;overflow:hidden}
body{position:relative;background:var(--white);font-family:"Open Sans",Arial,sans-serif;color:var(--text)}
a{color:inherit;text-decoration:none}

/* header */
.site-header{position:absolute;left:0;top:0;width:1200px;height:167px}
.brand{position:absolute;left:86px;top:68px;font-size:37px;font-weight:600;color:var(--ink);letter-spacing:-.3px}
.brand span{color:var(--blue)}
.main-nav{position:absolute;right:86px;top:77px;display:flex;gap:10px}
.main-nav a{font-size:15px;font-weight:600;color:#555;padding:9px 14px;text-transform:uppercase;letter-spacing:.2px}
.main-nav a.active{background:var(--blue);color:var(--white)}

/* hero */
.hero{position:absolute;left:0;top:167px;width:1200px;height:539px;background:radial-gradient(ellipse at 50% 30%,#d8d8d8 0%,#9c9c9c 45%,#3a3a3a 100%)}
.hero-caption{position:absolute;left:341px;top:311px;width:530px;height:136px;background:rgba(31,120,200,.82);color:var(--white);font-size:27px;line-height:45px;padding:22px 32px;text-transform:uppercase;font-weight:400}
.slider-dots{position:absolute;left:561px;top:497px;display:flex;gap:6px}
.slider-dots i{width:16px;height:16px;border-radius:50%;background:#e6e6e6}
.slider-dots i.on{background:var(--blue)}

/* services */
.services{position:absolute;left:0;top:706px;width:1200px;height:1080px}
.section-title{position:absolute;left:0;top:62px;width:1200px;text-align:center;font-size:39px;font-weight:300;color:#444}
.section-title span{color:var(--blue);font-weight:400}
.services-intro{position:absolute;left:96px;top:138px;width:1008px;text-align:center;font-size:13.5px;line-height:23px;color:var(--muted)}
.service-grid{position:absolute;left:71px;top:228px;display:grid;grid-template-columns:repeat(3,300px);column-gap:77px}
.service{height:289px;text-align:center}
.service-icon{display:block;margin:0 auto;width:84px;height:84px}
.service h3{margin-top:22px;font-size:21px;font-weight:400;color:var(--blue)}
.service hr{width:70px;border:0;border-top:1px solid #ddd;margin:14px auto 12px}
.service p{font-size:13px;line-height:22px;color:#777;white-space:nowrap}
.service a{display:block;margin-top:10px;font-size:13px;font-weight:600;color:var(--blue)}

/* welcome */
.welcome{position:absolute;left:86px;top:1854px;width:1028px;height:278px}
.welcome h2{font-size:30px;font-weight:400;color:var(--ink);margin-top:6px}
.welcome p{width:600px;margin-top:14px;font-size:13.5px;line-height:22px;color:#888}
.read-more{position:absolute;left:0;top:225px;width:144px;height:36px;border:2px solid var(--blue);border-radius:18px;color:var(--blue);font-size:14px;font-weight:600;display:flex;align-items:center;justify-content:center;gap:12px}
.promo{position:absolute;left:681px;top:0;width:347px;height:276px;overflow:hidden;background:linear-gradient(120deg,#d9e0e6 0%,#9fb0bd 45%,#6c7d8a 100%);color:var(--white)}
.promo-copy{position:absolute;left:150px;top:52px;width:180px}
.promo-copy h4{font-size:21px;font-weight:400;line-height:30px}
.promo-copy .tag{font-size:12px;line-height:17px;color:#dff0ff;margin-top:6px;white-space:normal}
.promo-copy .phone{font-size:15px;margin-top:10px}
.quote-btn{display:inline-block;margin-top:12px;background:var(--orange);color:var(--white);font-size:13px;padding:4px 12px}

/* blog */
.blog{position:absolute;left:86px;top:2208px;width:1028px;height:340px}
.blog h2{font-size:30px;font-weight:400;color:var(--ink)}
.post{position:absolute;left:0;width:600px;height:80px}
.post-thumb{position:absolute;left:0;top:0;width:66px;height:58px;background:linear-gradient(135deg,#c8d4de,#7d8d99)}
.post h3{position:absolute;left:83px;top:-6px;font-size:16.5px;font-weight:400;color:var(--blue)}
.post p{position:absolute;left:83px;top:22px;width:520px;font-size:13px;line-height:22px;color:#888}
.post p small{color:#b3b3b3;font-size:12px}

/* advert */
.ad{position:absolute;left:681px;top:5px;width:347px;height:327px;border:4px solid var(--red);background:var(--white);overflow:hidden;color:#222}
.ad-photo{position:absolute;left:0;top:128px;width:170px;height:155px;background:linear-gradient(180deg,#c9a07e 0%,#8a5a3c 100%)}
.ad-top{position:absolute;left:14px;top:10px;font-size:13px;font-weight:700;text-transform:uppercase}
.ad-head{position:absolute;left:0;top:28px;width:339px;text-align:center;font-size:23px;font-weight:800;color:var(--red);text-transform:uppercase}
.ad-sub{position:absolute;left:0;top:58px;width:339px;text-align:center;font-size:24px;font-weight:800;text-transform:uppercase}
.ad-nopmi{position:absolute;left:0;top:94px;width:339px;text-align:center;font-size:16px;font-weight:700}
.ad-details{position:absolute;left:174px;top:128px;width:160px;text-align:center}
.ad-name{font-size:16px;font-weight:800;color:var(--red);text-transform:uppercase;line-height:20px}
.ad-role{font-size:10px;font-weight:600;text-transform:uppercase}
.ad-num{font-size:14px;font-weight:700;line-height:20px;margin-top:3px}
.ad-states{font-size:11px;font-weight:600;margin-top:3px}
.ad-lender{font-size:12px;font-weight:600;margin-top:10px;display:flex;align-items:center;justify-content:center;gap:6px}
.ad-lender i{width:10px;height:10px;background:#222}
.ad-band{position:absolute;left:0;bottom:0;width:339px;height:36px;background:#111;color:var(--white);font-size:15px;font-weight:700;text-transform:uppercase;display:flex;align-items:center;padding-left:14px}

/* newsletter */
.newsletter{position:absolute;left:0;top:2572px;width:1200px;height:194px;background:linear-gradient(100deg,#1a6fc0 0%,#1f7ad0 55%,#2a86d8 56%,#1c74c8 100%)}
.newsletter h2{position:absolute;left:86px;top:104px;font-size:34px;font-weight:400;color:var(--white)}
.subscribe-form{position:absolute;left:747px;top:110px;display:flex}
.subscribe-form .field{width:238px;height:44px;border:1px solid rgba(255,255,255,.6);color:var(--white);font-size:13px;padding:0 16px;display:flex;align-items:center;background:rgba(255,255,255,.05)}
.subscribe-form .btn{width:127px;height:44px;background:var(--blue-dark);color:var(--white);font-size:15px;display:flex;align-items:center;justify-content:center}

/* footer */
.site-footer{position:absolute;left:0;top:2766px;width:1200px;height:360px;background:linear-gradient(180deg,#333 0%,var(--footer) 100%)}
.footer-col{position:absolute;top:40px}
.footer-col h4{font-size:17px;font-weight:400;color:var(--white);margin-bottom:12px;text-transform:uppercase}
.footer-col li{list-style:none;font-size:14px;line-height:33px;color:#ddd}
.contact-line{display:flex;align-items:flex-start;gap:10px;font-size:14px;color:#ddd;line-height:24px;margin-top:6px}
.social{display:flex;gap:8px;margin-top:34px}
.social i{width:28px;height:28px;border-radius:50%;background:#777}
.copyright{position:absolute;left:0;top:286px;width:1200px;height:74px;background:var(--footer-dark);border-top:1px solid #444}
.copyright p{position:absolute;left:92px;top:28px;font-size:13px;color:#ddd}
</style>
</head>
<body>

<header class="site-header">
  <div class="brand"><span>CLINICIAN</span> HARBOR COLLECTIVE</div>
  <nav class="main-nav">
    <a class="active" href="#">Home</a>
    <a href="#">About Us</a>
    <a href="#">Services</a>
    <a href="#">Contact</a>
  </nav>
</header>

<section class="hero" role="img" aria-label="Black and white photograph of an adult hand and a child's hand reaching toward each other">
  <div class="hero-caption">Maecenas sed diam eget risvari us blandit sit amet non</div>
  <div class="slider-dots"><i class="on"></i><i></i><i></i><i></i></div>
</section>

<section class="services">
  <h2 class="section-title">OUR <span>SERVICES</span></h2>
  <p class="services-intro">Claritas est etiam processus dynamicus, qui sequitur mutationem consuetudium lectorum. Mirum est notare quam littera gothica, quam nunc putamus parum claram, ut aliquip ex ea commodo consequat. Duis autem vel eum iriure dolor in hendrerit in vulputate velit esse molestie consequat, vel illum</p>

  <div class="service-grid">
    <div class="service">
      <svg class="service-icon" viewBox="0 0 84 84"><rect x="15" y="15" width="54" height="54" rx="4" transform="rotate(45 42 42)" fill="var(--blue)"/><circle cx="42" cy="42" r="10" fill="none" stroke="#fff" stroke-width="3"/><circle cx="42" cy="42" r="4" fill="#fff"/><g stroke="#fff" stroke-width="4"><line x1="42" y1="27" x2="42" y2="31"/><line x1="42" y1="53" x2="42" y2="57"/><line x1="27" y1="42" x2="31" y2="42"/><line x1="53" y1="42" x2="57" y2="42"/></g></svg>
      <h3>Disability Insurance</h3><hr>
      <p>Claritas est eteus dynamicuiniqui sequtatiem<br>conetlaritasdynamicusClaritas est.</p>
      <a href="#">Click here to contact me &gt;&gt;</a>
    </div>
    <div class="service">
      <svg class="service-icon" viewBox="0 0 84 84"><rect x="15" y="15" width="54" height="54" rx="4" transform="rotate(45 42 42)" fill="var(--blue)"/><path d="M28 50 h8 l8 4 h10 l4-4" fill="none" stroke="#fff" stroke-width="3"/><circle cx="46" cy="36" r="6" fill="none" stroke="#fff" stroke-width="3"/></svg>
      <h3>Life Insurance</h3><hr>
      <p>Claritas est eteus dynamicuiniqui sequtatiem<br>conetlaritasdynamicusClaritas est.</p>
      <a href="#">Click here to contact me &gt;&gt;</a>
    </div>
    <div class="service">
      <svg class="service-icon" viewBox="0 0 84 84"><rect x="15" y="15" width="54" height="54" rx="4" transform="rotate(45 42 42)" fill="var(--blue)"/><rect x="32" y="28" width="20" height="28" fill="none" stroke="#fff" stroke-width="3"/><g stroke="#fff" stroke-width="2"><line x1="36" y1="36" x2="48" y2="36"/><line x1="36" y1="42" x2="48" y2="42"/><line x1="36" y1="48" x2="48" y2="48"/></g></svg>
      <h3>Retirement Planning</h3><hr>
      <p>Claritas est eteus dynamicuiniqui sequtatiem<br>conetlaritasdynamicusClaritas est.</p>
      <a href="#">Click here to contact me &gt;&gt;</a>
    </div>
    <div class="service">
      <svg class="service-icon" viewBox="0 0 84 84"><rect x="15" y="15" width="54" height="54" rx="4" transform="rotate(45 42 42)" fill="var(--blue)"/><path d="M26 38 L42 31 L58 38 L42 45 Z" fill="#fff"/><path d="M33 42 v7 q9 5 18 0 v-7" fill="#fff"/></svg>
      <h3>Student Loan Advisors</h3><hr>
      <p>Claritas est eteus dynamicuiniqui sequtatiem<br>conetlaritasdynamicusClaritas est.</p>
      <a href="#">Click here to contact me &gt;&gt;</a>
    </div>
    <div class="service">
      <svg class="service-icon" viewBox="0 0 84 84"><rect x="15" y="15" width="54" height="54" rx="4" transform="rotate(45 42 42)" fill="var(--blue)"/><rect x="31" y="28" width="20" height="27" fill="none" stroke="#fff" stroke-width="3"/><line x1="42" y1="50" x2="55" y2="35" stroke="#fff" stroke-width="4"/></svg>
      <h3>Employment Contract</h3><hr>
      <p>Claritas est eteus dynamicuiniqui sequtatiem<br>conetlaritasdynamicusClaritas est.</p>
      <a href="#">Click here to contact me &gt;&gt;</a>
    </div>
    <div class="service">
      <svg class="service-icon" viewBox="0 0 84 84"><rect x="15" y="15" width="54" height="54" rx="4" transform="rotate(45 42 42)" fill="var(--blue)"/><circle cx="42" cy="35" r="7" fill="#fff"/><path d="M29 56 q13-16 26 0 Z" fill="#fff"/></svg>
      <h3>Accountants</h3><hr>
      <p>Claritas est eteus dynamicuiniqui sequtatiem<br>conetlaritasdynamicusClaritas est.</p>
      <a href="#">Click here to contact me &gt;&gt;</a>
    </div>
    <div class="service">
      <svg class="service-icon" viewBox="0 0 84 84"><rect x="15" y="15" width="54" height="54" rx="4" transform="rotate(45 42 42)" fill="var(--blue)"/><path d="M28 42 L42 30 L56 42" fill="none" stroke="#fff" stroke-width="3"/><rect x="32" y="42" width="20" height="13" fill="#fff"/><rect x="39" y="46" width="6" height="9" fill="var(--blue)"/></svg>
      <h3>Real Estate Agents</h3><hr>
      <p>Claritas est eteus dynamicuiniqui sequtatiem<br>conetlaritasdynamicusClaritas est.</p>
      <a href="#">Click here to contact me &gt;&gt;</a>
    </div>
    <div class="service">
      <svg class="service-icon" viewBox="0 0 84 84"><rect x="15" y="15" width="54" height="54" rx="4" transform="rotate(45 42 42)" fill="var(--blue)"/><g stroke="#fff" stroke-width="4" stroke-linecap="round"><line x1="32" y1="32" x2="52" y2="52"/><line x1="52" y1="32" x2="32" y2="52"/></g></svg>
      <h3>Physician Mortgages</h3><hr>
      <p>Claritas est eteus dynamicuiniqui sequtatiem<br>conetlaritasdynamicusClaritas est.</p>
      <a href="#">Click here to contact me &gt;&gt;</a>
    </div>
    <div class="service">
      <svg class="service-icon" viewBox="0 0 84 84"><rect x="15" y="15" width="54" height="54" rx="4" transform="rotate(45 42 42)" fill="var(--blue)"/><rect x="29" y="32" width="26" height="20" rx="2" fill="none" stroke="#fff" stroke-width="3"/><circle cx="37" cy="40" r="3" fill="#fff"/><line x1="43" y1="40" x2="50" y2="40" stroke="#fff" stroke-width="2"/><line x1="33" y1="47" x2="50" y2="47" stroke="#fff" stroke-width="2"/></svg>
      <h3>Personal Loans</h3><hr>
      <p>Claritas est eteus dynamicuiniqui sequtatiem<br>conetlaritasdynamicusClaritas est.</p>
      <a href="#">Click here to contact me &gt;&gt;</a>
    </div>
  </div>
</section>

<section class="welcome">
  <h2>Welcome to our website</h2>
  <p>Claritas est etiam processus dynamicus, qui sequitur mutationem consuetudium lectorum. Mirum est notare quam littera gothica, quam nunc putamus parum claram, anteposuerit litterarum formas humanitatis per dignissim qui blandit facer possim assum.<br>Duis autem vel eum iriure dolor in hendrerit in vulputate velit esse molestie consequat, vel illum dolore eu feugiat nulla facilisis at vero eros et accumsan et iusto odio dignissim into qui blandit praesent luptatum zzril delenit facer possim assum.</p>
  <a class="read-more" href="#">Read More
    <svg width="16" height="12" viewBox="0 0 16 12"><path d="M1 6 H14 M9 1 L14 6 L9 11" fill="none" stroke="currentColor" stroke-width="2"/></svg>
  </a>
  <div class="promo" role="img" aria-label="Photograph of a physician's hand holding a stethoscope">
    <div class="promo-copy">
      <h4>Disablity Insurance for Physicians</h4>
      <p class="tag">Empowering physicians<br>to contact their income</p>
      <p class="phone">+61 555 010 234</p>
      <span class="quote-btn">Get Quote</span>
    </div>
  </div>
</section>

<section class="blog">
  <h2>Recent Blog Posts</h2>
  <article class="post" style="top:72px">
    <div class="post-thumb" role="img" aria-label="Blog post thumbnail photograph"></div>
    <h3>Ut wisi enim ad minim veniam quis nostrud</h3>
    <p>Mirum est notare quam littera gothica, quam nunc putamus parum claram, antepo sueirit litterarum mirum est notare quam littera gothica. <small>1 hour ago</small></p>
  </article>
  <article class="post" style="top:172px">
    <div class="post-thumb" role="img" aria-label="Blog post thumbnail photograph of doctors"></div>
    <h3>Claritas est etiam processus dynamicus</h3>
    <p>Mirum est notare quam littera gothica, quam nunc putamus parum claram, antepo sueirit litterarum mirum est notare quam littera gothica. <small>1 hour ago</small></p>
  </article>
  <article class="post" style="top:272px">
    <div class="post-thumb" role="img" aria-label="Blog post thumbnail photograph of a medical team"></div>
    <h3>Eodem modo typi, qui nunc nobis videntur parum clari</h3>
    <p>Mirum est notare quam littera gothica, quam nunc putamus parum claram, antepo sueirit litterarum mirum est notare quam littera gothica. <small>1 hour ago</small></p>
  </article>

  <aside class="ad">
    <div class="ad-top">The Bank of Ashmere</div>
    <div class="ad-head">Doctor and Dentist</div>
    <div class="ad-sub">100% Loan Program</div>
    <div class="ad-nopmi">NO PMI</div>
    <div class="ad-photo" role="img" aria-label="Portrait photograph of the mortgage loan officer"></div>
    <div class="ad-details">
      <div class="ad-name">Marlene Hollis</div>
      <div class="ad-role">Mortgage Loan Officer</div>
      <div class="ad-num">615.555.0184</div>
      <div class="ad-num">NMLSR# 400127</div>
      <div class="ad-states">AL, FL, GA, SC, TN</div>
      <div class="ad-lender"><i></i>Bank of Ashmere</div>
      <div class="ad-lender"><i></i>Corvane</div>
    </div>
    <div class="ad-band">22 Years of Experience</div>
  </aside>
</section>

<section class="newsletter">
  <h2>Subscribe to our Newsletter</h2>
  <div class="subscribe-form">
    <div class="field">E-mail Address</div>
    <div class="btn">SUBSCRIBE</div>
  </div>
</section>

<footer class="site-footer">
  <div class="footer-col" style="left:95px">
    <h4>Links</h4>
    <ul><li>Privacy Policy</li><li>About Us</li><li>Track Order</li><li>Store Locator</li><li>Brand Houses</li><li>Gift Cards</li></ul>
  </div>
  <div class="footer-col" style="left:325px">
    <h4>Links</h4>
    <ul><li>Typi non haben</li><li>Successful Campaigns</li><li>New Campaigns</li><li>Ending Soon</li><li>Most Funded Campaigns</li><li>lorem ipsum</li></ul>
  </div>
  <div class="footer-col" style="left:611px">
    <h4>Links</h4>
    <ul><li>Typi non haben</li><li>Successful Campaigns</li><li>New Campaigns</li><li>Ending Soon</li><li>Most Funded Campaigns</li><li>lorem ipsum</li></ul>
  </div>
  <div class="footer-col" style="left:869px">
    <h4>Contact</h4>
    <div class="contact-line">
      <svg width="16" height="18" viewBox="0 0 16 18"><path d="M3 1 L6 1 L7 5 L5 7 Q7 11 10 12 L12 10 L15 11 L15 14 Q9 17 4 11 Q0 6 3 1 Z" fill="#999"/></svg>
      <span>916 555 0142</span>
    </div>
    <div class="contact-line" style="margin-top:16px">
      <svg width="16" height="20" viewBox="0 0 16 20"><path d="M8 1 A6 6 0 0 1 14 7 Q14 11 8 19 Q2 11 2 7 A6 6 0 0 1 8 1 Z" fill="#999"/><circle cx="8" cy="7" r="2.4" fill="#2f2f2f"/></svg>
      <span>4820 Larkspur Ridge Dr. #210<br>Fernhollow, CA 95999</span>
    </div>
    <div class="social" aria-label="Social media links"><i></i><i></i><i></i><i></i></div>
  </div>
  <div class="copyright"><p>Copyright ©2013. All Rights Reserved.</p></div>
</footer>

</body>
</html>
```